Brochure Design Project

We need a brochure designed for our company, specifically targeted at our corporate business customers ... Banks, Financial Services, Government. The brochure needs to detail our services and what we have to offer.

It may be a brochure/booklet that we can give to clients when we meet them. It needs to have a very corporate look and feel and needs to align with our colour palette and logo.

Information is held on our website www.veltrexworldservices.com

Thank you everyone for being part of this project.  It was a very hard decision.

Target Market(s)

Corporate business and clients including banks, financial services, insurance and government.

Industry/Entity Type

Business

Requirements
Must have
• Must have a corporate and global feel to it.
Must have our logo and same or similar colour palette.

```html
<!DOCTYPE html>
<html lang="en">
<head>
<meta charset="utf-8">
<title>Veltrex World Services – Brochure Spread</title>
<link href="https://fonts.googleapis.com/css2?family=Open+Sans:wght@300;400;600;700&display=swap" rel="stylesheet">
<style>
  :root {
    --backdrop: #cbcbcb;
    --paper: #ffffff;
    --brand-blue: #3f7abd;
    --navy: #1d2e5e;
    --band-grey: #808285;
    --rule: #8fb2dc;
    --ink-white: #ffffff;
  }
  * { margin: 0; padding: 0; box-sizing: border-box; }
  html, body { width: 1200px; height: 1000px; overflow: hidden; background: var(--backdrop); }
  body { position: relative; font-family: "Open Sans", Arial, sans-serif; }

  .spread {
    position: absolute; left: 110px; top: 138px; width: 990px; height: 700px;
    background: var(--paper);
    box-shadow: 8px 6px 10px rgba(0,0,0,0.28);
  }
  .spread-art { position: absolute; inset: 0; }
  .spine { position: absolute; left: 495px; top: 0; width: 1px; height: 700px; background: rgba(0,0,0,0.08); }

  .cover-title { position: absolute; left: 235px; top: 44px; color: var(--ink-white); }
  .cover-title h1 { font-weight: 400; font-size: 38px; line-height: 1; letter-spacing: 0.2px; }
  .cover-title p { font-size: 14px; line-height: 18px; margin-top: 6px; font-weight: 400; }

  .cover-url { position: absolute; left: 25px; top: 666px; font-size: 13px; font-weight: 700; color: var(--navy); }

  .brand { position: absolute; text-align: center; color: var(--navy); font-weight: 700; }
  .brand-dot { display: block; margin: 0 auto; border-radius: 50%; background: var(--brand-blue); }
  .brand-name { display: block; letter-spacing: 0.5px; line-height: 1.1; }
  .brand--cover { left: 345px; top: 614px; width: 130px; }
  .brand--cover .brand-dot { width: 32px; height: 32px; margin-bottom: 6px; }
  .brand--cover .brand-name { font-size: 12px; }
  .brand--back { left: 714px; top: 632px; width: 80px; }
  .brand--back .brand-dot { width: 20px; height: 20px; margin-bottom: 4px; }
  .brand--back .brand-name { font-size: 7.5px; }

  .rule { position: absolute; left: 536px; width: 407px; height: 1px; background: var(--rule); }
  .rule--top { top: 67px; }
  .rule--bottom { top: 292px; }

  .testimonials { position: absolute; left: 587px; top: 93px; width: 310px; color: var(--ink-white); }
  .testimonials h2 { font-weight: 400; font-size: 19px; margin-bottom: 3px; }
  .testimonials p { font-size: 7.8px; line-height: 12.8px; }
  .testimonials .lead { position: relative; padding-left: 19px; }
  .testimonials .quote-mark { position: absolute; left: 1px; top: -3px; font-size: 18px; font-weight: 700; font-style: normal; }

  .contact {
    position: absolute; left: 631px; top: 345px; width: 220px; height: 204px;
    border-left: 1px solid var(--rule); border-right: 1px solid var(--rule);
    color: var(--ink-white); font-size: 12px; line-height: 13.8px;
  }
  .contact address { font-style: normal; position: absolute; left: 19px; top: 15px; }
  .contact .company { font-weight: 700; }
  .contact .reach { position: absolute; right: 19px; top: 142px; text-align: right; line-height: 15.5px; }
</style>
</head>
<body>
  <div class="spread">
    <svg class="spread-art" width="990" height="700" viewBox="0 0 990 700">
      <defs>
        <linearGradient id="sky" x1="0" y1="0" x2="0" y2="1">
          <stop offset="0" stop-color="#1f3c7a"/>
          <stop offset="0.25" stop-color="#2f66b0"/>
          <stop offset="0.6" stop-color="#8fb9e6"/>
          <stop offset="0.82" stop-color="#d6e3ef"/>
          <stop offset="1" stop-color="#a9acb0"/>
        </linearGradient>
        <linearGradient id="badge" x1="0" y1="0" x2="1" y2="1">
          <stop offset="0" stop-color="#9ec4ea"/>
          <stop offset="1" stop-color="#3c6fa8"/>
        </linearGradient>
      </defs>
      <path class="edge-band" d="M0,0 H990 V597 C850,648 600,614 495,449 C380,614 120,642 0,601 Z" fill="var(--band-grey)"/>
      <path d="M0,0 H495 V452 C380,600 120,625 0,585 Z" fill="url(#sky)" role="img" aria-label="Photograph of a boardroom table with chairs set under a blue sky with white clouds"/>
      <path d="M495,0 H990 V580 C850,630 600,600 495,452 Z" fill="var(--brand-blue)"/>
      <g fill="none" stroke="#3a6fb0" stroke-width="3" opacity="0.8">
        <circle cx="567" cy="32" r="23"/>
        <circle cx="745" cy="32" r="23"/>
        <circle cx="900" cy="32" r="23"/>
      </g>
      <circle cx="112" cy="594" r="52" fill="#111"/>
      <circle cx="112" cy="594" r="44" fill="url(#badge)" role="img" aria-label="Photograph of a business handshake in front of an office tower"/>
    </svg>
    <div class="spine"></div>

    <div class="cover-title">
      <h1>Specialists in</h1>
      <p>Transformational Change &amp;<br>Sustainable Solutions</p>
    </div>

    <div class="cover-url">www.veltrexworldservices.com</div>

    <div class="brand brand--cover">
      <span class="brand-dot"></span>
      <span class="brand-name">VELTREX WORLD SERVICES</span>
    </div>

    <div class="rule rule--top"></div>
    <section class="testimonials">
      <h2>Testimonials</h2>
      <p class="lead"><span class="quote-mark">//</span>VWS have become the 'go to' practitioners that organisations call upon when they need a remedy and they need it fast! They have an ability to cut through complexity and provide clarity on the way forward quickly and efficiently."</p>
      <p>"Put simply VWS helps companies remediate critical, and in many cases intractable problems."</p>
      <p>"From Re-engineering to "Sustainable" Transformation and change, VWS can help find a way forward through the most complex blockers."</p>
      <p>"We wanted to transform our Organisation but were unsure of how to bring it all together. VWS supported us in creating a clear path forward managing all the moving parts. The result has been first class!"</p>
    </section>
    <div class="rule rule--bottom"></div>

    <div class="contact">
      <address>
        <span class="company">Veltrex World Services Pty Ltd</span><br>
        PO Box 418<br>
        Harbour Street North<br>
        Victoria 8120<br>
        AUSTRALIA
      </address>
      <div class="reach">
        +61 (03) 5550 2841<br>
        info@veltrexworldservices.com<br>
        www.veltrexworldservices.com
      </div>
    </div>

    <div class="brand brand--back">
      <span class="brand-dot"></span>
      <span class="brand-name">VELTREX WORLD SERVICES</span>
    </div>
  </div>
</body>
</html>
```